Business Card Design

RETAIL HIGH END CONTEMPORARY WOMEN'S CLOTHING STORE
MODERN, SIMPLE, CLEAN, COOL

WE ARE ALL ABOUT NY and CALIF STYLE.... CLASSY but EDGY..
COOLEST DENIM , Trendsetting, NEUTRAL Pallettes,
Collections : Fig and Stone, Dorian Vesk, PMW, K47, QTB
Don't need names of collections on card. thats just good info
for designer of card.

WOULD LIKE THE FONT TO BE INTERESTING, but CLEAN
We are on facebook daily with photos of outfits we put together
which you can look up and friend us.... MolvaHarbor
Also on instagram .
Open to options on color and size, but need cool and fresh.

Contact Information for Business Card

DELLA 5417 Larkmoor Rd. #309 Ember Court Arcade..Va. Beach, Va. 23987
Phone 757.386.5049 Fax 757.386-2613 EMAIL..DELLAMODE@QUILLBOX.COM

```html
<!DOCTYPE html>
<html lang="en">
<head>
<meta charset="utf-8">
<title>Della Business Card</title>
<link rel="stylesheet" href="https://fonts.googleapis.com/css2?family=Yrsa:wght@700&family=Source+Sans+3:wght@400&display=swap">
<style>
  :root {
    --stage: #3d3e40;
    --card-light: #dcdde0;
    --card-dark: #070707;
    --ink-light: #eeeeee;
    --ink-dark: #141414;
    --silver-hi: #ffffff;
    --silver-mid: #b9babd;
    --silver-lo: #6f7073;
  }
  html, body {
    margin: 0;
    padding: 0;
    width: 1200px;
    height: 900px;
    overflow: hidden;
    background: var(--stage);
  }
  .canvas {
    position: relative;
    width: 1200px;
    height: 900px;
  }
  .business-card {
    position: absolute;
    left: 189px;
    top: 178px;
    width: 750px;
    height: 464px;
    background: var(--card-light);
    overflow: hidden;
  }
  .card-shapes {
    position: absolute;
    inset: 0;
    width: 750px;
    height: 464px;
  }
  .contact-block {
    position: absolute;
    left: 12px;
    top: 8px;
    margin: 0;
    font-family: "Yrsa", "Georgia", serif;
    font-weight: 700;
    font-size: 22px;
    line-height: 35px;
    letter-spacing: -0.4px;
    color: var(--ink-light);
    transform: scaleX(0.86);
    transform-origin: left top;
  }
  .contact-line {
    display: block;
    white-space: nowrap;
  }
  .company-name {
    position: absolute;
    right: 4px;
    bottom: 6px;
    margin: 0;
    font-family: "Source Sans 3", "Helvetica", sans-serif;
    font-weight: 400;
    font-size: 47px;
    line-height: 1;
    letter-spacing: -0.5px;
    color: var(--ink-dark);
    white-space: nowrap;
  }
</style>
</head>
<body>
<main class="canvas">
  <section class="business-card">
    <svg class="card-shapes" viewBox="0 0 750 464" aria-hidden="true">
      <defs>
        <linearGradient id="silver-edge" x1="0" y1="0" x2="0.3" y2="1">
          <stop offset="0" stop-color="var(--silver-lo)"/>
          <stop offset="0.55" stop-color="var(--silver-mid)"/>
          <stop offset="1" stop-color="var(--silver-hi)"/>
        </linearGradient>
      </defs>
      <path class="silver-sweep" d="M574 0 H 598 C 592 220, 510 380, 380 464 H 296 C 470 360, 560 200, 574 0 Z" fill="url(#silver-edge)"/>
      <path class="dark-panel" d="M0 0 H 578 C 562 200, 472 362, 300 464 H 0 Z" fill="var(--card-dark)" role="img" aria-label="Black panel with a faint dotted texture"/>
    </svg>
    <p class="contact-block">
      <span class="contact-line">DELLA 5417 Larkmoor Rd. #309 Ember Court Arcade..Va. Beach, Va. 23987</span>
      <span class="contact-line">EMAIL..DELLAMODE@QUILLBOX.COM</span>
      <span class="contact-line">Fax 757.386-2613</span>
      <span class="contact-line">Phone 757.386.5049</span>
    </p>
    <p class="company-name">Company Name</p>
  </section>
</main>
</body>
</html>
```